Letter and Envelope Design For Juniper Crest Realty

Please design a letter and an envelope incorporating our logo (See Attached). We are also launched a business card contest. Since we want them to match, please feel free to submit a design for both the business card and also the letter design and envelope.

Requirements
Must have
• The envelope, the letter and the business cards must match somehow connecting the designs. We want them to have something that holds them together besides the logo.

```html
<!DOCTYPE html>
<html lang="en">
<head>
<meta charset="utf-8">
<title>Juniper Crest Realty – Letterhead</title>
<link href="https://fonts.googleapis.com/css2?family=Open+Sans:wght@400;600;700&display=swap" rel="stylesheet">
<style>
  :root {
    --backdrop: #2f2f2f;
    --paper: #ffffff;
    --brand-blue: #2b3288;
    --brand-grey: #555759;
    --ink: #1e1e1e;
    --muted: #7a7a7a;
    --rule: #c9c9c9;
  }
  * { box-sizing: border-box; margin: 0; padding: 0; }
  html, body { width: 1200px; height: 960px; overflow: hidden; }
  body {
    background: var(--backdrop);
    font-family: "Open Sans", Arial, sans-serif;
    color: var(--ink);
    position: relative;
  }
  .letterhead {
    position: absolute;
    left: 282px; top: 30px;
    width: 636px; height: 900px;
    background: var(--paper);
    box-shadow: 0 6px 24px rgba(0,0,0,.45);
    overflow: hidden;
  }
  .brand {
    position: absolute; left: 58px; top: 62px;
    display: flex; align-items: center; gap: 10px;
  }
  .brand-dot {
    width: 40px; height: 40px; border-radius: 50%;
    border: 3px solid var(--brand-blue);
  }
  .brand-name {
    font-weight: 600; font-size: 17px; letter-spacing: 1.6px;
    color: var(--brand-blue); text-transform: uppercase; line-height: 1.2;
  }
  .contact {
    position: absolute; right: 58px; top: 56px;
    border-left: 1px solid var(--rule);
    padding-left: 10px;
    font-size: 9.5px; color: var(--muted); line-height: 1.6;
    list-style: none;
  }
  .contact li { display: flex; align-items: center; gap: 6px; }
  .contact svg { width: 9px; height: 9px; fill: var(--brand-blue); flex: none; }
  .letter-body {
    position: absolute; left: 96px; top: 200px; width: 460px;
    font-size: 12.5px; line-height: 1.7;
  }
  .date { margin-bottom: 24px; }
  .recipient { margin-bottom: 26px; }
  .recipient .to-line { margin-bottom: 2px; }
  .recipient address { font-style: normal; padding-left: 14px; }
  .salutation { margin-bottom: 6px; }
  .letter-body p.copy { margin-bottom: 12px; }
  .closing { margin-top: 48px; padding-left: 86px; }
  .signature { margin-top: 28px; }
  .signature strong { display: block; font-weight: 700; }
  .footer-address {
    position: absolute; right: 58px; bottom: 42px;
    font-size: 10px; color: var(--muted);
  }
  .footer-band { position: absolute; left: 0; bottom: 0; width: 636px; height: 22px; }
</style>
</head>
<body>
  <main class="letterhead">
    <header>
      <div class="brand">
        <span class="brand-dot"></span>
        <span class="brand-name">Juniper Crest Realty</span>
      </div>
      <ul class="contact">
        <li><svg viewBox="0 0 10 10"><path d="M2 0.5l2 2-1 1.2c.6 1.3 1.6 2.3 2.8 2.8l1.2-1 2 2-1.4 1.8C3.8 9 1 6.2.4 2z"/></svg>555-210-4471</li>
        <li><svg viewBox="0 0 10 10"><rect x="1.5" y="0.5" width="7" height="9" rx="1"/></svg>555-210-4472</li>
        <li><svg viewBox="0 0 10 10"><path d="M0 2h10v6H0z M0 2l5 3.5L10 2" /></svg>hello@junipercrest.example</li>
        <li><svg viewBox="0 0 10 10"><circle cx="5" cy="5" r="4.5"/></svg>www.junipercrest.example</li>
      </ul>
    </header>

    <section class="letter-body">
      <p class="date">Date: 20 November 2018</p>
      <div class="recipient">
        <p class="to-line">To</p>
        <address>Willowmere Garden Ltd.<br>48 Alder Row, Suite# B<br>Leeds, UK LS2 7QX</address>
      </div>
      <p class="salutation">Dear Hart,</p>
      <p class="copy">Lorem Ipsum is simply dummy text of the printing and typesetting industry. Lorem Ipsum has been the industry's standard dummy text ever since the 1500s, when an unknown printer took a galley of type and scrambled it to make a type specimen book. It has survived not only five centuries, but also the leap into electronic typesetting, remaining essentially unchanged. It was popularised in the 1960s with the release of Typecraft sheets containing Lorem Ipsum passages, and more recently with desktop publishing software like Pagewright Studio including versions of Lorem Ipsum.</p>
      <p class="copy">Lorem Ipsum is simply dummy text of the printing and typesetting industry. Lorem Ipsum has been the industry's.</p>
      <div class="closing">
        <p>Thanking you</p>
        <p class="signature"><strong>Daniel Hart</strong>Director</p>
      </div>
    </section>

    <footer>
      <p class="footer-address">48 Alder Row, Suite # B, Leeds, UK LS2 7QX</p>
      <svg class="footer-band" viewBox="0 0 636 22" preserveAspectRatio="none" aria-hidden="true">
        <polygon points="0,0 372,0 364,22 0,22" fill="var(--brand-grey)"/>
        <polygon points="378,0 636,0 636,22 370,22" fill="var(--brand-blue)"/>
      </svg>
    </footer>
  </main>
</body>
</html>
```